Jewelry Manufacturing & Repair business needs advertising mailout - 9x4 flyer

Need new double sided flyer designed for an insert into a mailout. Want 9x4 (vertical design) to fit in 9.5" x 4.125" envelopes. Company based out of Louisiana called "Lem Travis Manufacturing." Been in business for 45 years. We specialize in custom jewelry design and casting on the wholesale level. We are a full service trade shop offering CAD design, casting services, basic and advanced jewelry repair. Most of our customers are drawn to the fact that they talk directly with the owner/designer of the company each time they call. I've attached several images of CAD renders we've built and of our logo. I've also attached a copy of an old mailout we sent out 10 years ago that I designed myself (and it needed a lot of work). The business information listed in this old mailout is correct, except that we’ve been in business 45 years now. I would like the final design to be "business bold," portraying business strength and stability. I like shades of blue, or a gold/silver color scheme. Logo is black and white. Need double sided.

Looking for project to be less wordy than the 10 yr old mailout. Don’t need the “example scenario” in this flyer.
Updates

The weekend has made the 2 day timeframe very tight. Would like to extend timeframe, but I will select a design on Monday at 3:00 pm (USA Central time).

Target Market(s)

Retail Jewelry Stores

Industry/Entity Type

Jewelry

Colors
cfdeed
0455a3
3176b5
85acd3

Requirements
Must have
• All contact information.
Nice to have
• Purpose of this flyer is to get new accounts for our business. We want something that the retail jewelry store will notice something that will make them not throw away immediately, but instead hold onto for the future.
• This upcoming Christmas season is usually very busy for retail stores, so we can help take some of the overflow of work and still meet deadlines. With our help, they shouldn't have to turn any customer away.
Should not have
• We will be partnering in this mailout with a sister wholesale diamond company. Therefore, we don't want to mention that our company sells any diamonds, as we want to leave that part up to our sister company.

```html
<!DOCTYPE html>
<html lang="en">
<head>
<meta charset="utf-8">
<title>Lem Travis Manufacturing – Mailout Flyer</title>
<link rel="stylesheet" href="https://fonts.googleapis.com/css2?family=Oswald:wght@500&family=Merriweather:wght@700&family=Hind:wght@400;500;600&display=swap">
<style>
  :root{
    --stage:#aebbbd;
    --paper:#ffffff;
    --swirl:#e6eaee;
    --blue:#1f5bf0;
    --ink:#111111;
    --glow:rgba(31,91,240,.35);
  }
  *{box-sizing:border-box;margin:0;padding:0}
  html,body{width:1200px;height:1200px;overflow:hidden;background:var(--stage)}
  body{position:relative;font-family:"Hind",sans-serif;color:var(--ink)}
  .flyer{position:absolute;top:96px;width:448px;height:1008px;overflow:hidden;
    background:
      radial-gradient(ellipse 420px 180px at 20% 45%,var(--swirl),transparent 70%),
      radial-gradient(ellipse 380px 160px at 85% 70%,var(--swirl),transparent 70%),
      radial-gradient(ellipse 360px 140px at 60% 20%,#eef1f4,transparent 70%),
      var(--paper);}
  .flyer--front{left:104px}
  .flyer--back{left:651px}
  .brand{position:absolute;left:149px;top:19px;width:150px;height:105px;display:flex;align-items:center;justify-content:center;gap:8px}
  .brand-mark{width:12px;height:12px;background:var(--ink)}
  .brand-name{font-family:"Hind",sans-serif;font-weight:600;font-size:19px;line-height:1.05;color:var(--ink)}
  .title-band{position:absolute;left:0;top:143px;width:100%;height:37px;background:var(--blue);
    color:#fff;font-family:"Oswald",sans-serif;font-weight:500;font-size:27px;line-height:37px;text-align:center;letter-spacing:.2px}
  .tagline{position:absolute;left:0;top:183px;width:100%;text-align:center;color:var(--blue);
    font-size:15px;font-weight:500;font-variant:small-caps}
  .photo{position:absolute;border:2px solid var(--blue);box-shadow:0 0 14px var(--glow)}
  .pitch{position:absolute;left:30px;top:822px;width:388px;text-align:center}
  .pitch h2{font-family:"Merriweather",serif;font-size:17px;color:var(--blue);margin-bottom:8px}
  .pitch p{font-size:12.2px;line-height:15.4px;margin-bottom:12px}
  .footer-band{position:absolute;left:0;bottom:0;width:100%;height:16px;background:var(--blue)}
  .section-title{position:absolute;left:46px;font-family:"Merriweather",serif;font-size:21px;color:var(--ink);
    border-bottom:3px solid var(--blue);padding-bottom:1px;line-height:1.15}
  .section-text{position:absolute;left:48px;width:356px;font-size:15.2px;line-height:19px}
  .offer-list{position:absolute;left:46px;list-style:none;font-size:15.2px}
  .offer-list li{height:23px;display:flex;align-items:center;gap:8px}
  .offer-list svg{width:11px;height:11px;flex:none}
  .contact-head{position:absolute;left:45px;top:808px;font-family:"Merriweather",serif;font-size:21px;color:var(--blue);font-weight:700}
  .contact-company{position:absolute;left:47px;top:842px;font-size:15px;font-weight:600;color:var(--blue)}
  .contact-line{position:absolute;left:48px;display:flex;align-items:flex-start;gap:9px;font-size:15px;line-height:19px}
  .contact-line svg{width:14px;height:14px;flex:none;margin-top:2px}
  .contact-line strong{font-weight:600}
</style>
</head>
<body>

<section class="flyer flyer--front">
  <div class="brand"><span class="brand-mark"></span><span class="brand-name">Lem Travis<br>Mfg</span></div>
  <div class="title-band">Lem Travis Manufacturing, LLC</div>
  <div class="tagline">Top Quality Craftsmanship, Friendly Personal Service</div>

  <div class="photo" role="img" aria-label="Stacked gold and silver diamond rings" style="left:29px;top:237px;width:167px;height:167px;background:radial-gradient(circle at 50% 50%,#d9cfb2,#c5ccd6 60%)"></div>
  <div class="photo" role="img" aria-label="Two gold cluster rings on gray" style="left:251px;top:237px;width:167px;height:167px;background:radial-gradient(circle at 50% 50%,#9a9486,#75787a 70%)"></div>
  <div class="photo" role="img" aria-label="Mixed metal wedding bands with gold inlay" style="left:114px;top:389px;width:221px;height:221px;background:linear-gradient(180deg,#dfe2ea,#b9bcc4 60%,#8e9198)"></div>
  <div class="photo" role="img" aria-label="Rose gold and white gold solitaire rings on black" style="left:29px;top:597px;width:167px;height:167px;background:radial-gradient(circle at 45% 45%,#4a3a36,#0b0b0b 70%)"></div>
  <div class="photo" role="img" aria-label="Stacked gold and rose gold bands" style="left:251px;top:597px;width:167px;height:167px;background:linear-gradient(160deg,#d7c6ad,#f1ece4 55%,#d9b98a)"></div>

  <div class="pitch">
    <h2>Are you looking for a way to increase profits?</h2>
    <p>Recent research shows that a large percentage of customers who actively seek out a new jewelry store do so because they need some type of repair service. Additionally, customer loyalty and satisfaction are based on a store’s ability to offer a complete range of services.</p>
    <p>Lem Travis Manufacturing can provide that highly skilled jeweler needed to take your business to the next level. We will work directly with you to meet all your customer’s needs, while maintaining a personal level of service that you will enjoy.</p>
  </div>
  <div class="footer-band"></div>
</section>

<section class="flyer flyer--back">
  <div class="brand"><span class="brand-mark"></span><span class="brand-name">Lem Travis<br>Mfg</span></div>

  <h2 class="section-title" style="top:139px">Who We Are:</h2>
  <p class="section-text" style="top:180px">We are a family operated business, serving the jewelry industry for over 35 years. Our experience provides us with a vast knowledge of the industry, as well as best practices for each unique item. We pride ourselves in quality craftsmanship with fast, honest, and courteous service.</p>

  <h2 class="section-title" style="top:298px">What We Offer:</h2>
  <ul class="offer-list" style="top:342px">
    <li><svg viewBox="0 0 12 12"><path d="M1 6.5l3 3 7-8" fill="none" stroke="#1f5bf0" stroke-width="1.6"/></svg>Basic &amp; advanced jewelry repair</li>
    <li><svg viewBox="0 0 12 12"><path d="M1 6.5l3 3 7-8" fill="none" stroke="#1f5bf0" stroke-width="1.6"/></svg>Custom hand carved wax modeling</li>
    <li><svg viewBox="0 0 12 12"><path d="M1 6.5l3 3 7-8" fill="none" stroke="#1f5bf0" stroke-width="1.6"/></svg>CAD / CAM services for intricate detail</li>
    <li><svg viewBox="0 0 12 12"><path d="M1 6.5l3 3 7-8" fill="none" stroke="#1f5bf0" stroke-width="1.6"/></svg>Gold &amp; Platinum casting</li>
    <li><svg viewBox="0 0 12 12"><path d="M1 6.5l3 3 7-8" fill="none" stroke="#1f5bf0" stroke-width="1.6"/></svg>Furnish waxes, raw castings, or finished products</li>
  </ul>

  <h2 class="section-title" style="top:465px">How it works:</h2>
  <p class="section-text" style="top:505px">The majority of our business is done safely and securely through one of the major parcel services (Swiftline, Parcelwing, Coastal Post). Utilizing insured overnight delivery, you have the option to have your jewelry back to you within a couple days.</p>

  <div class="photo" role="img" aria-label="Engagement rings on fabric" style="left:45px;top:623px;width:105px;height:141px;background:linear-gradient(160deg,#c9d2d8,#9fb0b8 60%,#d9c28a)"></div>
  <div class="photo" role="img" aria-label="Diamond rings on violet backdrop" style="left:172px;top:623px;width:105px;height:141px;background:radial-gradient(circle at 50% 45%,#b9aef0,#7f6fe0 70%)"></div>
  <div class="photo" role="img" aria-label="Colored gemstone rings on dark backdrop" style="left:298px;top:623px;width:105px;height:141px;background:radial-gradient(circle at 50% 55%,#3a3d46,#15161a 75%)"></div>

  <div class="contact-head">Call Lem or Carter Travis</div>
  <div class="contact-company">Lem Travis Manufacturing, LLC</div>
  <div class="contact-line" style="top:864px">
    <svg viewBox="0 0 14 14"><path d="M7 13s-4.5-4.6-4.5-7.6a4.5 4.5 0 0 1 9 0C11.5 8.4 7 13 7 13z" fill="none" stroke="#1f5bf0"/><circle cx="7" cy="5.5" r="1.6" fill="none" stroke="#1f5bf0"/></svg>
    <span>18 Heron Court<br>Delhi, LA 71232</span>
  </div>
  <div class="contact-line" style="top:912px">
    <svg viewBox="0 0 14 14"><circle cx="7" cy="7" r="6.3" fill="none" stroke="#1f5bf0"/><path d="M4.6 3.8l1.3 1.4-.7 1a5 5 0 0 0 2.6 2.6l1-.7 1.4 1.3-.9 1.2C6.8 10.4 3.6 7.2 3.4 4.7z" fill="#1f5bf0"/></svg>
    <strong>1-888-555-0142</strong>
  </div>
  <div class="contact-line" style="top:940px">
    <svg viewBox="0 0 14 14"><rect x="1" y="3" width="12" height="8.5" fill="none" stroke="#1f5bf0"/><path d="M1 3l6 5 6-5" fill="none" stroke="#1f5bf0"/></svg>
    <span>carter@ltravismfg.com</span>
  </div>
  <div class="contact-line" style="top:968px">
    <svg viewBox="0 0 14 14"><circle cx="7" cy="7" r="6" fill="none" stroke="#1f5bf0"/><ellipse cx="7" cy="7" rx="2.6" ry="6" fill="none" stroke="#1f5bf0"/><path d="M1 7h12M2 4h10M2 10h10" stroke="#1f5bf0" stroke-width=".8"/></svg>
    <span>www.ltravismfg.com</span>
  </div>
</section>

</body>
</html>
```